Corvelle Strategies business card

I need a business card for my new strategic consulting LLC, Corvelle Strategies. We specialize in helping people who care about broadband technology and telecommunications policy, and we're based in Washington DC. I'm looking for a card that says smart, credible, future-facing and signals a high level of expertise. It's DC, so there's clearly a limit to how crazy we can go with this card, but I am looking for a design that reflects a company that is comfortable with technology, policy, and having a little bit fun. I'm uploading my logo below, and I'd like to have it be part of the card design in some fashion.
Target Market(s)
Telecommunications and technology policy professionals
Industry/Entity Type
Technology policy
Contact Information for Business Card
Name of business, my name (Glen Mosswater), email (glen@corvellestrategies-example.com) , phone number (202-555-0148)phone number

```html
<!DOCTYPE html>
<html lang="en">
<head>
<meta charset="utf-8">
<title>Corvelle Strategies business card</title>
<link href="https://fonts.googleapis.com/css2?family=Arimo:wght@400;700&display=swap" rel="stylesheet">
<style>
  :root {
    --stage: #3d3d3d;
    --brand-blue: #00539c;
    --brand-orange: #f5a123;
    --paper: #ffffff;
  }
  * { box-sizing: border-box; margin: 0; padding: 0; }
  html, body {
    width: 1200px; height: 1200px; overflow: hidden;
    background: var(--stage);
    font-family: "Arimo", Arial, sans-serif;
  }
  .stage { position: relative; width: 1200px; height: 1200px; }
  .card {
    position: absolute;
    width: 689px; height: 393px;
    border-radius: 26px;
    overflow: hidden;
  }
  .card-front { left: 266px; top: 158px; background: var(--paper); }
  .card-back { left: 263px; top: 653px; background: var(--brand-blue); }

  .wave { position: absolute; inset: 0; width: 100%; height: 100%; }

  .wordmark {
    position: absolute;
    display: flex; align-items: center; gap: 10px;
    font-weight: 700; white-space: nowrap;
  }
  .wordmark-dot { border-radius: 50%; background: var(--brand-orange); flex: none; }
  .card-front .wordmark { left: 52px; top: 56px; font-size: 32px; color: var(--brand-blue); }
  .card-front .wordmark-dot { width: 22px; height: 22px; }
  .card-back .wordmark {
    left: 50%; top: 50%; transform: translate(-50%, -50%);
    font-size: 46px; color: var(--paper); gap: 14px;
  }
  .card-back .wordmark-dot { width: 34px; height: 34px; }

  .person { position: absolute; left: 54px; top: 164px; }
  .person-name { font-size: 27px; font-weight: 700; color: var(--brand-blue); line-height: 1.1; }
  .person-title { font-size: 15px; font-weight: 400; color: var(--brand-orange); margin-top: 3px; }

  .contact-list {
    position: absolute; right: 40px; top: 278px;
    list-style: none; color: var(--paper); font-size: 16.5px;
  }
  .contact-item {
    display: flex; align-items: center; justify-content: flex-end;
    gap: 16px; height: 21px;
  }
  .contact-icon { width: 11px; height: 11px; flex: none; }
</style>
</head>
<body>
<main class="stage">
  <section class="card card-front" aria-label="Card front">
    <svg class="wave" viewBox="0 0 1108 633" preserveAspectRatio="none" aria-hidden="true">
      <path fill="var(--brand-orange)" d="M45,522 C120,552 200,560 262,548 C420,518 530,382 718,266 C860,180 960,138 1041,165 C960,150 860,190 730,285 C560,405 440,528 262,552 C190,560 120,552 45,522 Z"/>
      <path fill="var(--brand-blue)" stroke="var(--paper)" stroke-width="5" d="M-5,512 C80,552 160,566 245,557 C410,538 525,410 705,290 C860,190 980,145 1115,197 L1115,640 L-5,640 Z"/>
    </svg>

    <div class="wordmark">
      <span class="wordmark-text">Corvelle Strategies</span>
      <span class="wordmark-dot"></span>
    </div>

    <div class="person">
      <h1 class="person-name">Glen Mosswater</h1>
      <p class="person-title">President</p>
    </div>

    <ul class="contact-list">
      <li class="contact-item">
        <span>(202-555-0148)</span>
        <svg class="contact-icon" viewBox="0 0 24 24" aria-hidden="true"><path fill="var(--brand-orange)" d="M6.6 10.8c1.4 2.8 3.8 5.1 6.6 6.6l2.2-2.2c.3-.3.7-.4 1-.2 1.1.4 2.3.6 3.6.6.6 0 1 .4 1 1V20c0 .6-.4 1-1 1C10.6 21 3 13.4 3 4c0-.6.4-1 1-1h3.5c.6 0 1 .4 1 1 0 1.3.2 2.5.6 3.6.1.3 0 .7-.2 1z"/></svg>
      </li>
      <li class="contact-item">
        <span>glen@corvellestrategies-example.com</span>
        <svg class="contact-icon" viewBox="0 0 24 24" aria-hidden="true"><rect x="2" y="5" width="20" height="14" rx="1.5" fill="var(--brand-orange)"/><path d="M3 6.5l9 6.5 9-6.5" fill="none" stroke="var(--brand-blue)" stroke-width="1.8"/></svg>
      </li>
      <li class="contact-item">
        <span>www.corvellestrategies-example.com</span>
        <svg class="contact-icon" viewBox="0 0 24 24" aria-hidden="true"><circle cx="12" cy="12" r="10" fill="var(--brand-orange)"/><path d="M2 12h20M12 2c3 3 3 17 0 20M12 2c-3 3-3 17 0 20" fill="none" stroke="var(--brand-blue)" stroke-width="1.5"/></svg>
      </li>
    </ul>
  </section>

  <section class="card card-back" aria-label="Card back">
    <div class="wordmark">
      <span class="wordmark-text">Corvelle Strategies</span>
      <span class="wordmark-dot"></span>
    </div>
  </section>
</main>
</body>
</html>
```